Business Cards for Dutch Young Draughts Trust

A promotion card (business card size) for the promotion of the Dutch Young Draughts Trust "Stichting Kinderdamspel". It should be in the style of the website and the logo.

People that receive the card should be impressed that a profesisonal organization is working to get more children play chess. The business card should give them trust, and should motivate them to take part of the movement.

Target Market(s)

Sponsors, business people, teachers, other professionals

Industry/Entity Type

Non-Profit

Contact Information for Business Card

Kinderdamspel Nederland
team@kinderdamspel-voorbeeld.nl
www.kinderdamspel-voorbeeld.nl
023 781 3096
Pieter Moltplein 8, 2034 KR Haarlem

Font styles to use
Sans Serif

Requirements
Must have
• Slogan on the business card: geef ieder kind kinderdamspel
• Main Blue - #025C75 RGB 2-92-117
• Main Orange - #FF6600 RGB 255-102-0
• Secondary Blue dark - #01313e - RGB 1-49-62
• Photo of boy playing chess should be integrated on 1 side of the card
• Logo of Girl and Boy is key in the design
• Style should be professional, and express the joy and value of chess for children
• Card is meant to be used by many people, so there need to be some space on the card where one can write their own name on the card
Should not have
• Other colours than the mentioned colours in the must haves

```html
<!DOCTYPE html>
<html lang="nl">
<head>
<meta charset="utf-8">
<title>Stichting Kinderdamspel – visitekaartje</title>
<link rel="stylesheet" href="https://fonts.googleapis.com/css2?family=Roboto:wght@400;500;700&display=swap">
<style>
  :root {
    --main-blue: #025C75;
    --main-orange: #FF6600;
    --dark-blue: #01313e;
    --paper: #ffffff;
    --ink: #1c1c1c;
    --backdrop: #3a3a3c;
  }
  * { box-sizing: border-box; margin: 0; padding: 0; }
  html, body { width: 1200px; height: 1000px; overflow: hidden; }
  body {
    background: var(--backdrop);
    font-family: "Roboto", Arial, sans-serif;
    position: relative;
  }
  .card {
    position: absolute;
    left: 250px;
    width: 700px;
    height: 420px;
    border-radius: 26px;
    overflow: hidden;
    background: var(--paper);
  }
  .card--front { top: 50px; }
  .card--back { top: 530px; }

  /* front */
  .photo-player {
    position: absolute; left: 0; top: 0; width: 100%; height: 220px;
    background: linear-gradient(100deg, var(--dark-blue) 0%, var(--main-blue) 55%, var(--dark-blue) 100%);
  }
  .brand-band {
    position: absolute; left: 0; top: 220px; width: 100%; height: 80px;
    background: var(--paper);
    display: flex; align-items: center; justify-content: space-between;
    padding: 0 34px;
  }
  .photo-board {
    position: absolute; left: 0; top: 300px; width: 100%; height: 120px;
    background: linear-gradient(180deg, var(--main-blue) 0%, var(--dark-blue) 100%);
  }
  .slogan {
    font-weight: 500; color: var(--main-orange);
    font-size: 18px; white-space: nowrap;
  }

  .wordmark { display: flex; align-items: center; gap: 12px; }
  .wordmark__dot {
    width: 26px; height: 26px; border-radius: 50%;
    background: var(--main-orange);
    flex: none;
  }
  .wordmark__name {
    font-weight: 700; color: var(--main-blue);
    font-size: 28px; letter-spacing: -0.3px; white-space: nowrap;
  }

  /* back */
  .card--back .wordmark {
    position: absolute; left: 40px; top: 188px;
  }
  .card--back .wordmark__name { font-size: 25px; }
  .divider {
    position: absolute; left: 372px; top: 120px;
    width: 2px; height: 200px; background: var(--ink);
  }
  .contact {
    position: absolute; left: 392px; top: 128px; right: 20px;
    color: var(--ink);
  }
  .contact__org {
    font-weight: 700; color: var(--main-blue);
    font-size: 19px; letter-spacing: 0.5px; text-transform: uppercase;
    margin-bottom: 12px;
  }
  .contact__address { font-size: 16px; line-height: 21px; margin-bottom: 4px; }
  .contact__line {
    display: flex; align-items: center; gap: 8px;
    font-size: 16px; line-height: 25px; font-weight: 500;
  }
  .contact__line svg { width: 15px; height: 15px; flex: none; }
  .contact__web-accent { color: var(--main-orange); }
</style>
</head>
<body>

<section class="card card--front" aria-label="Voorkant kaart">
  <div class="photo-player" role="img" aria-label="Foto van een jongen in een rood shirt die schaakt"></div>
  <div class="brand-band">
    <div class="wordmark">
      <span class="wordmark__dot"></span>
      <span class="wordmark__name">Stichting Kinderdamspel</span>
    </div>
    <p class="slogan">geef ieder kind kinderdamspel</p>
  </div>
  <div class="photo-board" role="img" aria-label="Foto van een schaakbord met zwarte stukken"></div>
</section>

<section class="card card--back" aria-label="Achterkant kaart">
  <div class="wordmark">
    <span class="wordmark__dot"></span>
    <span class="wordmark__name">Stichting Kinderdamspel</span>
  </div>
  <div class="divider"></div>
  <div class="contact">
    <p class="contact__org">Kinderdamspel Nederland</p>
    <p class="contact__address">Pieter Moltplein 8,<br>2034 KR Haarlem</p>
    <p class="contact__line">
      <svg viewBox="0 0 24 24" aria-hidden="true"><path fill="var(--main-orange)" d="M6.6 10.8a15.1 15.1 0 0 0 6.6 6.6l2.2-2.2c.3-.3.7-.4 1-.2 1.1.4 2.3.6 3.6.6.6 0 1 .4 1 1V20c0 .6-.4 1-1 1A17 17 0 0 1 3 4c0-.6.4-1 1-1h3.5c.6 0 1 .4 1 1 0 1.3.2 2.5.6 3.6.1.3 0 .7-.2 1z"/></svg>
      023 781 3096
    </p>
    <p class="contact__line">
      <svg viewBox="0 0 24 24" aria-hidden="true"><rect x="2" y="5" width="20" height="14" rx="2" fill="var(--main-orange)"/><path d="M3 6l9 7 9-7" fill="none" stroke="#fff" stroke-width="1.6"/></svg>
      team@kinderdamspel-voorbeeld.nl
    </p>
    <p class="contact__line">
      <svg viewBox="0 0 24 24" aria-hidden="true"><circle cx="12" cy="12" r="9.5" fill="none" stroke="var(--main-orange)" stroke-width="2"/><path d="M2.5 12h19M12 2.5c3 3 3 16 0 19M12 2.5c-3 3-3 16 0 19" fill="none" stroke="var(--main-orange)" stroke-width="1.6"/></svg>
      <span>www.<span class="contact__web-accent">kinderdamspel-voorbeeld</span>.nl</span>
    </p>
  </div>
</section>

</body>
</html>
```